M&A仲介を行っている企業です。
売り/買い両方のクライアント向けのDMに同封する会社案内の作成をお願いします。
企業向けに発送するものなので、信頼感があり、デザイン的に洗練された感じを希望します。
記載いただきたい内容は添付の通りです。
サイズはA4を希望。
修正の可能性もあるため、パワーポイントでの納品をお願いします。
(10/5)添付ファイルの文章に誤字脱字があったため添付しなおしました。
(10/5)誤字脱字修正後の添付ファイル名→会社概要案内 修正後

弊社のカラーでうまくまとめていただいたこと、また、デザイン性と見やすさで選択させていただきました。

たくさんのご提案ありがとうございました。
また機会がございましたら是非お願いいたします

```html
<!DOCTYPE html>
<html lang="ja">
<head>
<meta charset="UTF-8">
<title>会社概要 | 株式会社ミライブリッジ</title>
<link rel="stylesheet" href="https://fonts.googleapis.com/css2?family=Noto+Sans+JP:wght@400;500;700&display=swap">
<style>
:root{
  --teal:#2e9e96;
  --teal-dark:#1f7f86;
  --blue:#1d67a8;
  --teal-pale:#e3f2f0;
  --line:#9fcfca;
  --ink:#333;
  --muted:#555;
  --paper:#fff;
}
*{box-sizing:border-box;margin:0;padding:0}
html,body{width:849px;height:1200px;overflow:hidden;background:var(--paper)}
body{font-family:"Noto Sans JP",sans-serif;color:var(--ink);position:relative}
.abs{position:absolute}

.page-title{left:34px;top:22px;font-size:21px;font-weight:700;color:var(--teal-dark);letter-spacing:.08em}
.title-rule{left:34px;top:52px;width:560px;height:3px;background:linear-gradient(90deg,var(--teal),var(--blue) 60%,transparent)}

.brand{right:34px;top:22px;display:flex;align-items:center;gap:8px}
.brand-mark{width:24px;height:24px;background:var(--teal)}
.brand-name{font-size:20px;font-weight:700;color:var(--blue);letter-spacing:.06em}

.profile{left:34px;top:64px;width:781px;border-collapse:collapse;font-size:10.5px}
.profile th,.profile td{border:1px solid var(--line);padding:4px 8px;text-align:left;vertical-align:middle;line-height:1.5}
.profile th{background:var(--teal-pale);font-weight:500;color:var(--teal-dark);width:104px}
.profile td.sub{background:#f3f9f8;width:150px}

.band{left:0;width:849px;height:34px;display:flex;align-items:center;padding-left:34px;color:#fff;font-size:18px;font-weight:700;letter-spacing:.06em;
  background:linear-gradient(90deg,var(--teal) 0%,var(--blue) 55%,rgba(29,103,168,.15) 100%)}

.box{top:350px;width:238px;height:210px;border:1.5px solid var(--teal);background:#fff}
.box-head{background:var(--teal);color:#fff;font-size:12.5px;font-weight:700;padding:4px 10px;display:flex;align-items:center;gap:6px}
.box-head::before{content:"";width:9px;height:9px;background:#fff}
.box ul{list-style:none;padding:7px 10px;font-size:9.5px;line-height:1.62}
.box li::before{content:"■";color:var(--teal);margin-right:3px;font-size:8px}
.box-buy{border-color:var(--blue)}
.box-buy .box-head{background:var(--blue)}
.box-buy li::before{color:var(--blue)}

.photo{background:linear-gradient(135deg,#cfe3ec,#9bbfd1 60%,#7fa7bd)}

.case-head{left:34px;width:781px;height:40px;border-bottom:2px solid var(--teal);display:flex;justify-content:space-between;align-items:flex-end;padding-bottom:4px}
.case-title{font-size:14.5px;font-weight:700;color:var(--blue)}
.case-scheme{font-size:10.5px;color:var(--muted);line-height:1.4;text-align:left}
.case-scheme b{color:var(--teal-dark);font-weight:700}
.case-text{left:34px;font-size:10.5px;line-height:1.85;color:var(--ink);text-align:justify}

.foot{left:0;bottom:0;width:849px;height:10px;background:linear-gradient(90deg,var(--teal),var(--blue))}
</style>
</head>
<body>

<h1 class="abs page-title">会社概要</h1>
<div class="abs title-rule"></div>
<div class="abs brand"><span class="brand-mark"></span><span class="brand-name">MIRAI BRIDGE</span></div>

<table class="abs profile">
  <tr><th>会社名</th><td colspan="2">株式会社ミライブリッジ</td><th>代表取締役</th><td>山田 健一</td></tr>
  <tr><th>設立日</th><td colspan="2">1998年9月10日</td><th>資本金</th><td>2,000万円</td></tr>
  <tr><th>所在地／連絡先</th><td colspan="4">【本社】<br>新潟県新潟市中央区本町通5-12-3 ／ 025-000-1234<br>【東京オフィス】<br>東京都港区芝大門3-8-1 汐見ビル4階 ／ 03-0000-5678</td></tr>
  <tr><th rowspan="3">事業内容</th><td class="sub">M&amp;Aアドバイザリー<br>事業</td><td colspan="3">・M&amp;A仲介、アドバイザリー<br>・企業再生、組織再編コンサルティング<br>・企業経営コンサルティング</td></tr>
  <tr><td class="sub">エージェント事業</td><td colspan="3">・スペシャリストの人材紹介</td></tr>
  <tr><td class="sub">ケアスタッフ事業</td><td colspan="3">・医療・介護特化型の人材サービス</td></tr>
</table>

<h2 class="abs band" style="top:306px">M&amp;Aアドバイザリー　具体的な業務</h2>

<div class="abs box" style="left:34px">
  <div class="box-head">譲渡企業様へ</div>
  <ul>
    <li>事業承継戦略の相談</li>
    <li>企業価値の算定</li>
    <li>譲渡スキームの提案</li>
    <li>譲受企業の選定</li>
    <li>譲渡の条件交渉</li>
    <li>M&amp;Aプロセスへのアドバイス</li>
    <li>交渉</li>
    <li>譲渡条件まとめのコーディネート</li>
    <li>企業概要書の作成</li>
    <li>クロージングのサポート</li>
  </ul>
</div>

<div class="abs box box-buy" style="left:282px">
  <div class="box-head">譲受企業様へ</div>
  <ul>
    <li>M&amp;A戦略</li>
    <li>企業の選定</li>
    <li>対象先の調査・分析</li>
    <li>交渉</li>
    <li>M&amp;Aの実施のために必要となるスキームの<br>　選定と条件面のアドバイス</li>
    <li>財務DD等各種調査のコーディネート</li>
    <li>譲渡企業との最終契約締結</li>
    <li>譲渡企業の統合サポート</li>
  </ul>
</div>

<div class="abs photo" style="left:534px;top:350px;width:281px;height:210px" role="img" aria-label="握手を交わすビジネスパーソンの写真"></div>

<h2 class="abs band" style="top:574px">M&amp;A 成功事例のご紹介</h2>

<div class="abs case-head" style="top:614px">
  <span class="case-title">【複数金融機関から借入あるも、再生型M&amp;Aで事業譲渡】</span>
  <span class="case-scheme"><b>スキーム：事業譲渡</b><br>介護事業者 ➡ 医療法人</span>
</div>
<p class="abs case-text" style="top:664px;width:520px">
入所系の介護施設を地域で運営しているオーナー社長が70代を迎え、後継者不在の問題を抱えていました。加えて過去の設備投資により複数の金融機関からの借入があり、財務状況は厳しい状態が続いていました。社長は従業員と入居者の生活を守ることを第一に考え、事業の存続に向けた相談を弊社へ寄せられました。弊社は金融機関との調整を進めながら、地域医療との連携を重視する医療法人を譲受先として選定しました。事業譲渡のスキームを採用することで借入の整理と雇用の継続を両立し、入居者へのサービスも途切れることなく引き継がれました。再生型M&amp;Aを前提とした交渉により、関係者全員が納得できる形での成約となりました。
</p>
<div class="abs photo" style="left:560px;top:664px;width:255px;height:148px" role="img" aria-label="介護施設で高齢者を支えるスタッフの写真"></div>

<div class="abs case-head" style="top:840px">
  <span class="case-title">【社員への承継からM&amp;Aへ切り替え、3ヶ月のスピード完了】</span>
  <span class="case-scheme"><b>スキーム：株式譲渡</b><br>建設業 ➡ 建設土木工事業</span>
</div>
<p class="abs case-text" style="top:890px;width:520px">
地元で工事を担ってきた建設会社の社長は、当初は長年勤める社員への承継を検討していました。しかし株式の買取資金や個人保証の引継ぎが大きな負担となり、社員側も承継を辞退する結果となりました。そこで弊社へご相談いただき、M&amp;Aへ方針を切り替えることになりました。弊社は事業エリアと技術の相乗効果が見込める建設土木工事会社を候補として提案し、双方のトップ面談を早期に実施しました。条件面の調整と調査を並行して進めたことで、ご相談から約3ヶ月という短期間で株式譲渡が完了しました。社員の雇用と取引先との関係も維持され、地域のインフラを支える事業は新たな体制のもとで成長を続けています。
</p>
<div class="abs photo" style="left:560px;top:890px;width:255px;height:150px" role="img" aria-label="工事現場で作業する建設スタッフの写真"></div>

<div class="abs foot"></div>
</body>
</html>
```